Women's Health Company needs business card

We need a business card for a USA based women's health care company. We use digital technology to enhance therapy prescribed by clinicians for their patients

```html
<!DOCTYPE html>
<html lang="en">
<head>
<meta charset="utf-8">
<title>Lunora Health — Stationery</title>
<link rel="stylesheet" href="https://fonts.googleapis.com/css2?family=Lato:wght@300;400;700&family=Arimo:wght@400&display=swap">
<style>
:root{
  --purple:#874f96;
  --teal:#5fb3ab;
  --paper:#f4f4f4;
  --bg:#e4e4e4;
  --ink:#222;
  --muted:#6a6a6a;
}
*{margin:0;padding:0;box-sizing:border-box}
html,body{width:1200px;height:942px;overflow:hidden}
body{background:var(--bg);position:relative;font-family:'Lato',sans-serif;color:var(--ink)}
.sheet{position:absolute;background:var(--paper);overflow:hidden;box-shadow:0 1px 3px rgba(0,0,0,.12)}
.brand{font-family:'Lato',sans-serif;font-weight:300;color:var(--teal);white-space:nowrap;letter-spacing:.5px}
.swoosh{position:absolute;right:0;bottom:0;display:block}
.contact{font-family:'Arimo',sans-serif;color:var(--muted);line-height:1.45}
.contact .gap{margin-top:4px}
.contact svg{width:6px;height:6px;margin-right:5px;vertical-align:middle}

/* Letterhead */
.letterhead{left:157px;top:150px;width:436px;height:617px}
.letterhead .brand{position:absolute;top:38px;left:0;width:100%;text-align:center;font-size:30px}
.letter{position:absolute;left:46px;top:179px;width:343px;font-size:7.1px;line-height:8.8px;text-align:justify}
.letter .salute{font-weight:700;margin-bottom:8px}
.letter p{margin-bottom:8.8px}
.letter .close{margin-top:22px}
.signature{width:100px;height:14px;margin-top:8px;background:linear-gradient(90deg,rgba(34,34,34,.18),rgba(34,34,34,.05))}
.letterhead .contact{position:absolute;left:45px;top:543px;font-size:7px}
.letterhead .web{position:absolute;left:328px;top:581px;font-family:'Arimo',sans-serif;font-size:7px;color:#fff}

/* Business cards */
.card{top:139px;width:227px;height:130px}
.card-front{left:625px}
.card-front .brand{position:absolute;left:22px;top:22px;font-size:20px}
.card-front .person{position:absolute;right:24px;top:17px;text-align:right}
.person .name{font-weight:700;color:var(--purple);font-size:7.2px}
.person .role{font-size:5px}
.card-front .details{position:absolute;right:24px;top:69px;text-align:right;color:#fff;font-size:5px;line-height:6.6px}
.card-back{left:897px;background:var(--purple)}
.card-back .brand{position:absolute;left:0;width:100%;top:50px;text-align:center;font-size:22px}

/* Envelope front */
.envelope{left:624px;top:298px;width:501px;height:217px}
.envelope .brand{position:absolute;left:37px;top:34px;font-size:30px}
.envelope .contact{position:absolute;left:37px;top:148px;font-size:7.2px}
.envelope .web{position:absolute;left:395px;top:187px;font-family:'Arimo',sans-serif;font-size:7.2px;color:#fff}

/* Envelope back */
.envelope-back{left:624px;top:550px;width:501px;height:217px;background:#f2f2f2}
.envelope-back .seams{position:absolute;inset:0}
.envelope-back .brand{position:absolute;left:0;width:100%;top:20px;text-align:center;font-size:22px}
</style>
</head>
<body>

<section class="sheet letterhead">
  <div class="brand">Lunora Health</div>
  <div class="letter">
    <div class="salute">Dear Mark Ellison,</div>
    <p>Lorem ipsum dolor sit amet, consectetuer adipiscing elit, sed diam nonummy nibh euismod tincidunt ut laoreet dolore magna aliquam erat volutpat. Ut wisi enim ad minim veniam, quis nostrud exerci tation ullamcorper suscipit lobortis nisl ut aliquip ex ea commodo consequat. Duis dolore te feugait nulla facilisi. Nam liber tempor cum soluta nobis eleifend option congue nihil imperdiet doming id quod mazim placerat facer possim assum. Lorem ipsum dolor sit amet, consectetuer adipiscing elit, sed diam nonummy nibh euismod tincidunt ut laoreet dolore magna aliquam erat volutpat. Ut wisi enim ad minim veniam, quis nostrud exerci tation ullamcorper suscipit lobortis nisl ut aliquip ex ea commodo consequat.</p>
    <p>Consectetuer adipiscing elit, sed diam nonummy nibh euismod tincidunt ut laoreet dolore magna aliquam erat volutpat. Ut wisi enim ad minim veniam, quis nostrud exerci tation ullamcorper suscipit lobortis nisl ut aliquip ex ea commodo consequat. Consectetuer adipiscing elit, sed diam nonummy nibh euismod tincidunt ut laoreet dolore magna aliquam erat volutpat. Ut wisi enim ad minim veniam, quis nostrud exerci tation ullamcorper suscipit lobortis nisl ut aliquip ex ea commodo consequat.</p>
    <p>Consectetuer adipiscing elit, sed diam nonummy nibh euismod tincidunt ut laoreet dolore magna aliquam erat volutpat. Ut wisi enim ad minim veniam, quis nostrud exerci tation ullamcorper suscipit lobortis nisl ut aliquip ex ea commodo consequat. Consectetuer adipiscing elit, sed diam nonummy nibh euismod tincidunt ut laoreet dolore magna aliquam erat volutpat. Ut wisi enim ad minim veniam, quis nostrud exerci tation ullamcorper suscipit lobortis nisl ut aliquip ex ea commodo consequat.</p>
    <div class="close">Sincerely Yours</div>
    <div class="signature" role="img" aria-label="Handwritten signature of Thomas Reyes"></div>
    <div>General Manager</div>
  </div>
  <div class="contact">
    PO Box 3000<br>Co. Street, Building/Suite<br>City/State, Zip Code
    <div class="gap"><svg viewBox="0 0 10 10"><path d="M2 1l2 0 1 2.5-1.3 1a6 6 0 0 0 2.8 2.8l1-1.3L10 7v2a1 1 0 0 1-1 1A9 9 0 0 1 0 1a1 1 0 0 1 1-1z" fill="var(--purple)"/></svg>555.014.2200</div>
    <div><svg viewBox="0 0 10 10"><rect x="0" y="2" width="10" height="6" fill="var(--purple)"/><path d="M0 2l5 3.5L10 2" stroke="#fff" stroke-width="1" fill="none"/></svg>hello@lunorahealth.com</div>
  </div>
  <svg class="swoosh" width="170" height="82" viewBox="0 0 170 82" preserveAspectRatio="none" aria-hidden="true">
    <path d="M0 82C40 30 85 0 115 2C138 3 156 12 170 20V82Z" fill="var(--purple)"/>
    <path d="M5 82C45 28 90 6 118 8C140 10 158 18 170 26" fill="none" stroke="var(--teal)" stroke-width="3"/>
  </svg>
  <div class="web">www.lunorahealth.com</div>
</section>

<section class="sheet card card-front">
  <div class="brand">Lunora Health</div>
  <div class="person">
    <div class="name">Daniel Hartwell</div>
    <div class="role">Managing Director</div>
  </div>
  <svg class="swoosh" width="190" height="92" viewBox="0 0 190 92" preserveAspectRatio="none" aria-hidden="true">
    <path d="M0 92C40 35 90 0 125 0C150 0 172 10 190 20V92Z" fill="var(--purple)"/>
    <path d="M6 92C48 33 95 6 128 6C152 6 174 16 190 26" fill="none" stroke="var(--teal)" stroke-width="3"/>
  </svg>
  <div class="details">
    PO Box 3000<br>Co. Street, Building/Suite<br>City/State, Zip Code<br>
    <span style="display:block;margin-top:4px">555.014.2200</span>hello@lunorahealth.com<br>www.lunorahealth.com
  </div>
</section>

<section class="sheet card card-back">
  <div class="brand">Lunora Health</div>
</section>

<section class="sheet envelope">
  <div class="brand">Lunora Health</div>
  <div class="contact">
    PO Box 3000<br>Co. Street, Building/Suite<br>City/State, Zip Code
    <div class="gap"><svg viewBox="0 0 10 10"><path d="M2 1l2 0 1 2.5-1.3 1a6 6 0 0 0 2.8 2.8l1-1.3L10 7v2a1 1 0 0 1-1 1A9 9 0 0 1 0 1a1 1 0 0 1 1-1z" fill="var(--purple)"/></svg>555.014.2200</div>
    <div><svg viewBox="0 0 10 10"><rect x="0" y="2" width="10" height="6" fill="var(--purple)"/><path d="M0 2l5 3.5L10 2" stroke="#fff" stroke-width="1" fill="none"/></svg>hello@lunorahealth.com</div>
  </div>
  <svg class="swoosh" width="215" height="102" viewBox="0 0 215 102" preserveAspectRatio="none" aria-hidden="true">
    <path d="M0 102C45 40 95 0 135 0C165 0 192 12 215 24V102Z" fill="var(--purple)"/>
    <path d="M6 102C50 38 100 7 138 7C166 7 194 19 215 31" fill="none" stroke="var(--teal)" stroke-width="3.5"/>
  </svg>
  <div class="web">www.lunorahealth.com</div>
</section>

<section class="sheet envelope-back">
  <svg class="seams" width="501" height="217" viewBox="0 0 501 217" aria-hidden="true">
    <path d="M0 217L14 55M501 217L487 55" stroke="#cfcfcf" stroke-width="1" fill="none"/>
    <path d="M0 0H501L486 62Q482 71 472 71H29Q19 71 15 62Z" fill="var(--purple)"/>
  </svg>
  <div class="brand">Lunora Health</div>
</section>

</body>
</html>
```